Label or packaging Design for Hair Care Line

Dear Designer,
We are Corvella, a brand known for our premium hairstyling tools, and we are excited to expand into hair care. We are currently looking for a talented designer to create the label designs for our entire luxury hair care line.
This project is crucial in establishing our visual identity in the hair care market, and we aim to position ourselves alongside premium brands such as LTP, Dorvane Hair Atelier, and Pelmi.
Project Scope
We need a cohesive label design for our hair care line, which includes:
5 products (e.g., shampoo, conditioner, hair oil, styling cream, and a hair mask).
The designs should include:
Front label: Highlighting the product name, key features, and branding.
Our goal is to achieve a design that communicates premium luxury with a touch of professionalism. Below are the specific guidelines to help you align with our vision:
Style and Inspiration
Think of brands like LTP, Dorvane Hair Atelier, and Pelmi.
Luxury and Minimalism: Clean lines, sophisticated typography, and an elegant color palette.
Subtle femininity: premium finishes like metallic accents (gold, silver, or rose gold).
Brand Personality
Premium: Reflecting high quality and exclusivity.
Modern & Professional: Appealing to a refined, professional audience but also suitable for lifestyle-oriented customers.
Warm & Empowering: A brand that celebrates confidence and individuality.
Color Palette
Neutral tones like black, white, accented with metallics (gold or silver) for a luxurious feel.
Colors that feel timeless and elegant rather than trendy or overly bright.
Typography
Use clean, modern fonts (preferably sans-serif or serif for a refined look).
Clear and legible for all product details while maintaining a high-end aesthetic.
Materials and Finishes
Packaging Shape
The label designs should suit a variety of bottle and jar shapes (e.g., cylindrical, flat, or rounded).
Keep scalability in mind so the identity remains consistent across different products.
Deliverables
To understand the aesthetic we are aiming for, here are some brands to use as inspiration:
LTP: For its minimalistic and modern approach.
Dorvane Hair Atelier: For its combination of luxury and professional appeal.
Pelmi: For its soft femininity and lifestyle branding.
we would like to see your designs applied to a variety of packaging types to get an overall impression of how the brand identity works across different product formats. This includes:
A squeeze bottle (e.g., for styling creams or conditioners).
A glass bottle with a dropper (e.g., for a luxurious hair oil).
A shampoo/conditioner bottle (standard pump or flip-top cap).
A spray bottle (e.g., for leave-in treatments or heat protectors).
By creating designs for these different packaging types, we can better evaluate how cohesive and versatile the brand identity will be across the entire product line.

Updates
As you may have noticed from the designs, they don’t quite align with our briefing. The look needs to be clean and professional, similar to Dorvane, LTP, and the other examples we provided. Please address this, and we’ll check it!

Target Market(s)
europe and us
Font styles to use
Other font styles liked:
- century gothic

Look and feel
Each slider illustrates characteristics of the customer's brand and the style your logo design should communicate.

```html
<!DOCTYPE html>
<html lang="en">
<head>
<meta charset="UTF-8">
<title>Corvella Styling Cream Label</title>
<link href="https://fonts.googleapis.com/css2?family=Outfit:wght@300;400&display=swap" rel="stylesheet">
<style>
  :root {
    --backdrop: #e9e9ea;
    --label-dark: #2b2b2c;
    --label-mid: #4a4a4b;
    --ink-light: #f4f4f2;
    --ink-soft: #cfcfcd;
    --rose-gold: #c9a08a;
    --rose-gold-deep: #8e6a5a;
  }
  * { margin: 0; padding: 0; box-sizing: border-box; }
  html, body {
    width: 1200px;
    height: 1200px;
    overflow: hidden;
    background: var(--backdrop);
    font-family: "Outfit", "Century Gothic", sans-serif;
  }
  .canvas {
    position: relative;
    width: 1200px;
    height: 1200px;
  }
  .label {
    position: absolute;
    left: 330px;
    top: 80px;
    width: 540px;
    height: 1040px;
    background: linear-gradient(90deg, var(--label-dark) 0%, var(--label-mid) 38%, var(--label-mid) 48%, var(--label-dark) 100%);
    color: var(--ink-light);
  }
  .brand-name {
    position: absolute;
    left: 270px;
    top: 360px;
    transform: translate(-50%, -50%) rotate(-90deg);
    font-weight: 300;
    font-size: 104px;
    letter-spacing: 0.01em;
    white-space: nowrap;
    color: var(--ink-light);
    line-height: 1;
  }
  .product-name {
    position: absolute;
    top: 706px;
    left: 0;
    width: 100%;
    text-align: center;
    font-weight: 400;
    font-size: 20px;
    letter-spacing: 0.38em;
    padding-left: 0.38em;
    color: var(--ink-light);
  }
  .emblem {
    position: absolute;
    top: 770px;
    left: 233px;
    width: 74px;
    height: 84px;
    border-radius: 50%;
    background: radial-gradient(circle, rgba(201,160,138,0.05) 30%, rgba(201,160,138,0.45) 60%, rgba(142,106,90,0.15) 75%, transparent 76%);
  }
  .description {
    position: absolute;
    top: 890px;
    left: 0;
    width: 100%;
    text-align: center;
    font-weight: 300;
    font-size: 8px;
    line-height: 1.3;
    color: var(--ink-soft);
  }
  .volume {
    position: absolute;
    top: 970px;
    left: 0;
    width: 100%;
    text-align: center;
    font-weight: 300;
    font-size: 14px;
    color: var(--ink-light);
  }
</style>
</head>
<body>
  <main class="canvas">
    <section class="label">
      <div class="brand-name">Corvella</div>
      <h1 class="product-name">STYLING CREAM</h1>
      <div class="emblem" role="img" aria-label="Rose-gold circular ornament of leaf shapes"></div>
      <p class="description">
        Lorem ipsum dolor sit amet, consectetur<br>
        adipiscing elit, sed do eiusmod tempor<br>
        incididunt ut labore et dolore magna aliqua<br>
        Ut enim ad minim veniam, quis tui estre efit<br>
        nostrud exercitation.
      </p>
      <p class="volume">100ml ℮</p>
    </section>
  </main>
</body>
</html>
```